Attractive Wall Posters wanted

We are designing posters for our outdoor wall to represent our brands.

(Portrait Layout: Measurements - Height 128cm, Width 108cm).

More information for each brand can be found on the website listed in the ppt attached.

Requirements
Must have
• The information included in PPT, the logo, the website and the short description
Nice to have
• Consistency across all posters
Should not have
• too cluttered designs

```html
<!DOCTYPE html>
<html lang="en">
<head>
<meta charset="utf-8">
<title>Learning Circle – Wall Poster</title>
<link href="https://fonts.googleapis.com/css2?family=Arimo:wght@400;700&family=Inter:wght@300;400;500&display=swap" rel="stylesheet">
<style>
  :root {
    --gold: #c89a2d;
    --band-grey: #e6e6e6;
    --copy-grey: #666666;
    --paper: #ffffff;
  }
  html, body {
    margin: 0;
    padding: 0;
    overflow: hidden;
    background: var(--paper);
  }
  .poster {
    position: relative;
    width: 1013px;
    height: 1200px;
    overflow: hidden;
    background: var(--paper);
    font-family: "Inter", "Helvetica Neue", Arial, sans-serif;
  }
  .poster__sweep {
    position: absolute;
    inset: 0;
    width: 1013px;
    height: 1200px;
  }
  .sweep__gold { fill: var(--gold); }
  .sweep__shade { fill: var(--band-grey); }

  .title {
    position: absolute;
    margin: 0;
    color: var(--gold);
    line-height: 1;
    letter-spacing: -1px;
  }
  .title__main {
    left: 78px;
    top: 200px;
    font-size: 94px;
    font-weight: 500;
  }
  .title__sub {
    left: 136px;
    top: 294px;
    font-size: 94px;
    font-weight: 300;
  }
  .website {
    position: absolute;
    left: 146px;
    top: 422px;
    margin: 0;
    font-size: 24px;
    color: var(--gold);
  }
  .tagline {
    position: absolute;
    left: 84px;
    top: 1056px;
    width: 320px;
    margin: 0;
    font-size: 15px;
    line-height: 19px;
    font-weight: 300;
    color: var(--copy-grey);
  }
  .brand-name {
    position: absolute;
    left: 736px;
    top: 1036px;
    margin: 0;
    font-family: "Arimo", Arial, sans-serif;
    font-size: 96px;
    font-weight: 700;
    letter-spacing: -4px;
    line-height: 1;
    color: var(--gold);
  }
</style>
</head>
<body>
  <main class="poster">
    <svg class="poster__sweep" viewBox="0 0 1013 1200" aria-hidden="true">
      <path class="sweep__shade" d="M1013 432 C830 590 690 860 588 1200 L624 1200 C720 900 860 650 1013 470 Z"/>
      <path class="sweep__gold" d="M668 0 C560 300 430 700 440 1200 L560 1200 C660 850 820 560 1013 392 L1013 0 Z"/>
    </svg>

    <h1 class="title title__main">Learning</h1>
    <p class="title title__sub">Circle</p>
    <p class="website">www.KLClearn.com</p>

    <p class="tagline">KLC is set up with the belief that everyone has a talent and that learning should be unique and revolve around our talents.</p>

    <p class="brand-name">KLC</p>
  </main>
</body>
</html>
```